Short presentation of new electrical engineering company

i just founded a new company and would like to send a short presentation to selected potential new customers. So they know that there is a new company and what we do. I am looking for a short presentation since i believe it is too long, nobody will read it. i need it in english and german, but i can provide both texts. i thought, it should be a short version of my existing homepage www.velunor.ch on paper Prefered format: A5 or A4 landscape folded. Reason is that i can send it easily with mail. The design should be technical, electrical engineering, provide the important information as contact information, some referenc work, and the range of service. i have no other design requirements. it should just look great ;-)

Target Market(s)

Production Companies which could be electrical engineer freelancers

Industry/Entity Type

Engineering

Font styles to use
Sans Serif

Requirements
Must have
• German and English Version Either A5 double side or A4 folded double side. Reason is that you have to send it by mail and do not want to fold it in the middle of the design
Nice to have
• Some different layouts as my drafts would be nice i am curious what else could be done

```html
<!DOCTYPE html>
<html lang="de">
<head>
<meta charset="utf-8">
<title>Velunor – Flyer</title>
<link href="https://fonts.googleapis.com/css2?family=Open+Sans:wght@400;600;700;800&display=swap" rel="stylesheet">
<style>
:root{
  --bg:#8f8f8f;
  --blue:#1e9ad6;
  --navy:#252a63;
  --navy-2:#3a3f82;
  --ink:#2b2b2b;
  --head-blue:#2a86c8;
  --line:#c9ccd6;
  --card:#f3f4f7;
  --white:#ffffff;
}
*{box-sizing:border-box;margin:0;padding:0}
html,body{width:1200px;height:788px;overflow:hidden;background:var(--bg);font-family:"Open Sans",Arial,sans-serif;color:var(--ink)}
.page{position:absolute;top:54px;width:524px;height:678px;background:var(--white);overflow:hidden}
.page--front{left:64px}
.page--back{left:614px}
.abs{position:absolute}

.brand{position:absolute;display:flex;align-items:center;gap:6px;color:var(--navy);font-weight:800;font-size:30px;letter-spacing:1px}
.brand__dot{width:12px;height:12px;background:var(--navy)}

.photo{position:absolute}
.hero{position:absolute;left:0;top:193px;width:524px;height:94px;background:var(--blue);color:var(--white)}
.hero__title{position:absolute;left:27px;top:12px;width:160px;font-size:15.5px;font-weight:700;line-height:20px}
.hero__rule{position:absolute;left:194px;top:16px;width:1px;height:68px;background:rgba(255,255,255,.6)}
.hero__text{position:absolute;left:212px;top:14px;width:285px;font-size:7px;line-height:10px;text-align:justify}
.hero__text p+p{margin-top:7px}

.service{position:absolute;width:143px;border:1px solid var(--line);background:var(--white)}
.service__head{height:19px;background:linear-gradient(90deg,var(--navy),var(--navy-2));color:var(--white);font-size:9.5px;font-weight:600;padding:4px 6px;display:flex;align-items:center;gap:8px;letter-spacing:.2px}
.service__head svg{width:18px;height:12px}
.service ul{list-style:none;padding:5px 6px 0 6px}
.service li{position:relative;padding-left:10px;font-size:6.3px;line-height:8.2px;margin-bottom:3.4px}
.service li::before{content:"";position:absolute;left:1px;top:2px;width:4.5px;height:4.5px;border-radius:50%;background:var(--blue)}

.footer{position:absolute;left:0;top:619px;width:524px;height:45px;background:var(--navy);color:var(--white);font-size:6.8px;line-height:10px}
.footer__col{position:absolute;top:8px}
.footer__col + .footer__col{border-left:1px solid rgba(255,255,255,.35)}
.footer__web{font-weight:700;font-size:7.8px;margin-top:3px;display:block}
.footer-strip{position:absolute;left:0;top:664px;width:524px;height:14px;background:var(--blue)}

.refs-head{position:absolute;left:0;top:0;width:524px;height:56px;background:var(--blue)}
.refs-head h1{position:absolute;left:31px;top:30px;color:var(--white);font-size:17.5px;font-weight:700;letter-spacing:1.4px}
.ref{position:absolute;left:20px;width:484px;background:var(--card);border:1px solid #dcdee5}
.ref__img{position:absolute;left:7px;top:8px;width:142px}
.ref__scope{position:absolute;left:161px;top:6px;width:215px}
.ref__label{color:var(--head-blue);font-weight:700;font-size:10.5px;line-height:14px;margin-bottom:5px}
.ref__intro{font-size:6.7px;line-height:9px;margin-bottom:4px}
.ref__scope ul{list-style:none}
.ref__scope li{position:relative;padding-left:12px;font-size:6.7px;line-height:9px;margin-bottom:4px}
.ref__scope li.tick::before{content:"";position:absolute;left:1px;top:1px;width:3px;height:5px;border-right:1.3px solid var(--navy);border-bottom:1.3px solid var(--navy);transform:rotate(40deg)}
.ref__rule{position:absolute;left:383px;top:8px;width:1px;background:var(--head-blue)}
.ref__meta{position:absolute;left:392px;top:6px;font-size:8.2px;line-height:11px}
.ref__meta dt{color:var(--head-blue);font-weight:700;font-size:10.5px;line-height:13px}
.ref__meta dd{margin-bottom:6px}
</style>
</head>
<body>

<section class="page page--front">
  <div class="brand" style="left:168px;top:26px"><span class="brand__name">VELUNOR</span><span class="brand__dot"></span></div>

  <div class="photo" style="left:0;top:87px;width:210px;height:106px;background:linear-gradient(120deg,#9aa3a8,#dfe3e4 45%,#7d8a86)" role="img" aria-label="Reihenklemmen im Schaltschrank, Nahaufnahme"></div>
  <div class="photo" style="left:210px;top:87px;width:171px;height:106px;background:linear-gradient(150deg,#c9c3b6,#6d8a5a 50%,#3b3a3a)" role="img" aria-label="Elektronische Leiterplatte mit Bauteilen"></div>
  <div class="photo" style="left:381px;top:87px;width:143px;height:106px;background:linear-gradient(160deg,#b8bcbf,#e2e4e4 40%,#2f3a33)" role="img" aria-label="SPS-Module im Schaltschrank"></div>

  <div class="hero">
    <h2 class="hero__title">Gemeinsam Herausforderungen Meistern Und Ziele Erreichen</h2>
    <div class="hero__rule"></div>
    <div class="hero__text">
      <p>Die Firma Velunor Electrical Automation Engineering unterstützt Sie in Ihren Anliegen betreffend allen Bereichen der Elektro-technik und der Automation.</p>
      <p>Wir sind Spezialisten in dem entwerfen von Steuerungen, programmieren der SPS, erstellen von Visualisierungen, auslegen von Antriebsleistungen und der Inbetriebnahme aller Komponenten vor Ort. Dies jeweils unter Berücksichtigung aller gängigen Nor-men und Standards.</p>
    </div>
  </div>

  <div class="service" style="left:26px;top:318px;height:149px">
    <div class="service__head">ENGINEERING
      <svg viewBox="0 0 18 12" fill="none" stroke="#fff" stroke-width="1"><circle cx="9" cy="6" r="2.5"/><circle cx="9" cy="6" r="5"/></svg></div>
    <ul>
      <li>Beratungen, Konzepte und Machbar-keitsstudien zu Automatisierungsanla-gen</li>
      <li>Service und Support</li>
      <li>Entwicklung von Produkten</li>
      <li>Innovationen im Bereich Elektrotech-nik</li>
      <li>Verbesserungen bestehender Abläufe oder Produkten</li>
      <li>Gesamt-Projektleitung</li>
      <li>Offerten und Preisschätzungen</li>
    </ul>
  </div>
  <div class="service" style="left:192px;top:318px;height:149px">
    <div class="service__head">PROGRAMMIERUNG
      <svg viewBox="0 0 30 12" fill="none" stroke="#fff" stroke-width="1" style="width:28px"><rect x="1" y="2" width="28" height="9"/><path d="M5 6h6M14 4v5M19 6h6"/></svg></div>
    <ul>
      <li>Sentrix Step 7</li>
      <li>Sentrix Studio Portal</li>
      <li>Schaller Electric CoMachine</li>
      <li>Rockmont RXLogic 5000</li>
      <li>Erstellen von Visualisierungen auf ver-schiedenen Plattformen</li>
      <li>Programmieren von Desktopanwen-dungen mit C#</li>
      <li>KOP, FUP, AWL oder SCL</li>
    </ul>
  </div>
  <div class="service" style="left:354px;top:318px;height:149px">
    <div class="service__head">ANTRIEBSTECHNIK</div>
    <ul>
      <li>Auslegung von Antriebsleistungen</li>
      <li>Evaluation der geeigneten Antriebsart</li>
      <li>Parametrieren von Frequenzumrich-tern verschiedener Hersteller</li>
      <li>Verbessern des Wirkungsgrades</li>
    </ul>
  </div>

  <div class="service" style="left:26px;top:485px;height:113px">
    <div class="service__head">STEUERUNGEN
      <svg viewBox="0 0 30 12" fill="none" stroke="#fff" stroke-width="1" style="width:28px"><path d="M1 6h8M21 6h8M9 2h12v8H9zM15 0v2"/></svg></div>
    <ul>
      <li>Planen von Automatisierungslösungen</li>
      <li>Erstellen von Konzepten und Schemas</li>
      <li>Modernisieren von bestehenden Steu-erungen</li>
      <li>Hersteller-Unabhängig</li>
    </ul>
  </div>
  <div class="service" style="left:192px;top:485px;height:113px">
    <div class="service__head">INBETRIEBNAHMEN</div>
    <ul>
      <li>Inbetriebnahmen von Steuerungen, Anlagen und Antrieben Weltweit</li>
      <li>Lösungsfindung und beheben von auftretenden Problemen vor Ort</li>
      <li>Durchführen der geforderten Ab-schlusstests nach erfolgreicher Inbe-triebnahme</li>
    </ul>
  </div>
  <div class="service" style="left:354px;top:485px;height:113px">
    <div class="service__head">RISIKOANALYSEN</div>
    <ul>
      <li>Durchführen von Gefährdungsabschät-zungen</li>
      <li>Minimieren der Gefahren gemäss EN 13849</li>
      <li>Erstellen der nötigen Nachweisdoku-menten</li>
      <li>Software Reviews von bestehen-dem Code</li>
    </ul>
  </div>

  <footer class="footer">
    <div class="footer__col" style="left:25px;width:170px">KONTAKT<br>MARC KELLER: +41 79 000 12 34<br>M.KELLER@VELUNOR.CH</div>
    <div class="footer__col" style="left:181px;width:168px;padding-left:14px">Velunor Gmbh, Marc Keller<br>Lindenweg 8, 6300 Zug<span class="footer__web">www.velunor.ch</span></div>
    <div class="footer__col" style="left:350px;width:170px;padding-left:16px">KONDITIONEN BIS 01/08/2018<br>INLAND CH: 112 CHF exkl./Std.<br>AUSLAND: ZUS. 100FR Spesen/Tag.</div>
  </footer>
  <div class="footer-strip"></div>
</section>

<section class="page page--back">
  <header class="refs-head"><h1>REFERENZEN</h1></header>

  <article class="ref" style="top:66px;height:110px">
    <div class="ref__img" style="height:94px;background:linear-gradient(110deg,#b9bda8,#d8dac9 45%,#2e4f86)" role="img" aria-label="Schaltschrank mit Antriebsmotor"></div>
    <div class="ref__scope">
      <div class="ref__label">Lieferumfang</div>
      <ul>
        <li class="tick">Entwurf von dem mechanischen Aufbau in einer 3D CAD Zeichnung</li>
        <li class="tick">Auslegung der Antriebseinheit</li>
        <li class="tick">Vorbereiten der Zeichnungen für CNC Fräsen</li>
        <li>Inbetriebnahme und erstellen der Dokumentation.</li>
      </ul>
    </div>
    <div class="ref__rule" style="height:92px"></div>
    <dl class="ref__meta"><dt>Kunde</dt><dd>Hofer Automation</dd><dt>Ausführung</dt><dd>2016</dd><dt>Ort</dt><dd>New York</dd></dl>
  </article>

  <article class="ref" style="top:185px;height:137px">
    <div class="ref__img" style="top:18px;height:94px;background:linear-gradient(180deg,#4d5a78,#2b3a8e 40%,#c6c8cc)" role="img" aria-label="Schaltschrank mit Frequenzumrichtern"></div>
    <div class="ref__scope">
      <div class="ref__label">Lieferumfang</div>
      <p class="ref__intro">Unterstützung als Freelancer für ein Projektteam.</p>
      <ul>
        <li class="tick" style="margin-bottom:3.8px">Entwurf des Schemas mit den neuen Frequenzumrichtern</li>
        <li class="tick" style="margin-bottom:3.8px">Anpassen der Schnittstellen</li>
        <li class="tick" style="margin-bottom:3.8px">Erstellen von Installationsanweisungen</li>
        <li class="tick" style="margin-bottom:3.8px">Inbetriebnahme vor Ort</li>
        <li class="tick" style="margin-bottom:3.8px">Abstimmung der Rockmont SPS auf die neuen FU</li>
        <li class="tick" style="margin-bottom:3.8px">Durchführen von Site Acceptance Tests</li>
        <li class="tick">Abnahme durch Prüfstelle Süd.</li>
      </ul>
    </div>
    <div class="ref__rule" style="height:120px"></div>
    <dl class="ref__meta"><dt>Kunde</dt><dd>Brenntec GmbH</dd><dt>Ausführung</dt><dd>2016</dd><dt>Ort</dt><dd>Deutschland</dd></dl>
  </article>

  <article class="ref" style="top:334px;height:107px">
    <div class="ref__img" style="height:92px;background:linear-gradient(135deg,#f2f2f4,#c9cbd0 50%,#eeeef0)" role="img" aria-label="3D-Modell einer Wellenaufhängung"></div>
    <div class="ref__scope">
      <div class="ref__label">Lieferumfang</div>
      <ul>
        <li class="tick">Evaluation der geeigneten Antriebseinheit</li>
        <li class="tick">Auslegung der Antriebsleistung</li>
        <li class="tick">Entwerfen der mechanischen Aufhängungen sowie Befes-tigung der Welle und deren Lagerung.</li>
      </ul>
    </div>
    <div class="ref__rule" style="height:90px"></div>
    <dl class="ref__meta"><dt>Kunde</dt><dd>Hofer Automation</dd><dt>Ausführung</dt><dd>2016</dd><dt>Ort</dt><dd>Schweiz</dd></dl>
  </article>

  <article class="ref" style="top:453px;height:110px">
    <div class="ref__img" style="height:94px;background:linear-gradient(180deg,#5d6e8c,#c9b99a 55%,#3a4650)" role="img" aria-label="Riesenrad vor Abendhimmel"></div>
    <div class="ref__scope">
      <div class="ref__label">Lieferumfang</div>
      <p class="ref__intro">Unterstützung als Freelancer für ein Projektteam.</p>
      <ul>
        <li class="tick">Programmierung der Hydraulikeinheit auf einer Sentrix SPS</li>
        <li class="tick">Erstellen von Abschlussprüfungen</li>
        <li class="tick">Unterstützung bei der Inbetriebnahme vor Ort</li>
        <li class="tick">Durchführen von SAT (Site Acceptance Tests)</li>
      </ul>
    </div>
    <div class="ref__rule" style="top:14px;height:86px"></div>
    <dl class="ref__meta" style="top:14px"><dt>Kunde</dt><dd>Brenntec GmbH</dd><dt>Ausführung</dt><dd>2015</dd><dt>Ort</dt><dd>Orlando</dd></dl>
  </article>

  <div class="brand" style="left:178px;top:576px"><span class="brand__name">VELUNOR</span><span class="brand__dot"></span></div>

  <footer class="footer">
    <div class="footer__col" style="left:25px;width:170px">KONTAKT<br>MARC KELLER: +41 79 000 12 34<br>M.KELLER@VELUNOR.CH</div>
    <div class="footer__col" style="left:181px;width:168px;padding-left:14px">Velunor Gmbh, Marc Keller<br>Lindenweg 8, 6300 Zug<span class="footer__web">www.velunor.ch</span></div>
    <div class="footer__col" style="left:350px;width:170px;padding-left:16px">KONDITIONEN BIS 01/08/2018<br>INLAND CH: 112 CHF exkl./Std.<br>AUSLAND: ZUS. 100FR Spesen/Tag.</div>
  </footer>
  <div class="footer-strip"></div>
</section>

</body>
</html>
```